Lantern - Web Design Project

We are seeking to have our website redesigned. Our current webpage is rather dated looking www.lantern-outcomes.com We will be utilizing similar content to explain our services as what is in the website now. We do not see it at a retail portal but rather a website for those inquiring about our services as a reference check so to speak.

We wish to have a look that is considered clean, fresh, contemporary and contains a business savvy vibe.

We prefer isolated white background and also wish to retain the integrity of our Logo and colour scheme.

We are looking for something that doesnt look like it was designed at home on sitemoose. We are hoping to find something that looks like it would reside on a tablet.
Updates

Hello designers!

We apologize for our tardiness as we have been quite preoccupied. We will be extending our invites to the end of January!

Hello All,

Please review our offer once again for updated requirements.  We are hoping to accept a design by months end.

Lantern

Target Market(s)

Business to business clients and Large manufacturers

Industry/Entity Type

Retail

Requirements
Must have
• Existing Logo

There must be an area dedicated to an intro video that will be incorporated on our landing page.

We require design of the other pages as well not only the landing page.

```html
<!DOCTYPE html>
<html lang="en">
<head>
<meta charset="utf-8">
<title>Lantern Performance Group</title>
<link rel="stylesheet" href="https://fonts.googleapis.com/css2?family=Ubuntu:wght@300;400;500;700&family=Rokkitt:wght@300;400&family=Arimo:wght@400;700&display=swap">
<style>
  :root{
    --page:#efefef;
    --ink:#3c3c3c;
    --muted:#5a5a5a;
    --red:#e2231a;
    --red-dark:#c71c0e;
    --red-light:#f04a1c;
    --field:#7d7d7d;
    --footer:#dadada;
    --dark-btn:#1e1e1e;
  }
  *{margin:0;padding:0;box-sizing:border-box}
  html,body{width:1200px;height:1121px;overflow:hidden}
  body{background:var(--page);font-family:"Arimo",Arial,sans-serif;color:var(--ink);position:relative}
  .abs{position:absolute}

  .brand{left:155px;top:30px;display:flex;align-items:center;gap:10px;font-family:"Ubuntu",sans-serif;font-weight:500;font-size:46px;color:#4a4443;letter-spacing:-1px}
  .brand-dot{width:14px;height:14px;border-radius:50%;background:var(--red)}
  .phone{right:121px;top:34px;font-family:"Ubuntu",sans-serif;font-size:18px;color:#3a3a3a}
  .search{left:807px;top:73px;width:272px;height:23px;border-radius:3px;background:#3a3d40;color:#fff;font-family:"Ubuntu",sans-serif;font-size:12px;padding:4px 10px}
  .search svg{position:absolute;right:9px;top:4px}

  .nav{left:0;top:105px;width:1200px;height:40px;background:linear-gradient(#f04c1e,#d3230c);border-top:1px solid #ff6a3a}
  .nav ul{list-style:none;position:absolute;left:120px;top:0;display:flex;height:40px}
  .nav li{font-family:"Ubuntu",sans-serif;font-weight:500;font-size:13px;color:#fff;line-height:40px;padding:0 23px;margin-right:6px}
  .nav li.active{background:#c81f0c;box-shadow:inset 0 0 0 1px #e0401e}

  .hero{left:0;top:145px;width:1200px;height:330px;background:linear-gradient(160deg,#2a2418 0%,#3a3326 35%,#5a5040 55%,#2b2b2b 75%,#1d2018 100%)}
  .hero-light{left:0;top:145px;width:1200px;height:330px;background:linear-gradient(165deg,transparent 40%,rgba(255,220,170,.25) 55%,rgba(255,150,60,.25) 62%,transparent 72%)}
  .play{left:565px;top:235px}
  .caption{left:0;top:399px;width:1200px;height:76px;background:rgba(0,0,0,.72);color:#fff;font-family:"Ubuntu",sans-serif;font-weight:500;font-size:16px;line-height:19px;padding:7px 130px 0 134px;letter-spacing:.75px}
  .caption .by{margin-top:6px}
  .dots{left:1016px;top:458px;display:flex;gap:8px}
  .dots span{width:10px;height:10px;background:#ddd;border-radius:1px}
  .dots span.on{background:var(--red)}

  .welcome{left:120px;top:500px;width:960px;font-family:"Ubuntu",sans-serif;font-weight:400;font-size:27px;color:#333;display:flex;align-items:center;gap:14px}
  .welcome em{font-style:normal;color:var(--red)}
  .welcome i{flex:1;height:1px;background:#dcdcdc;margin-top:4px}
  .intro{left:122px;top:548px;width:958px;font-family:"Ubuntu",sans-serif;font-weight:300;font-size:14.5px;line-height:24px;color:#444;text-align:justify}
  .rule{left:120px;top:643px;width:960px;height:2px;background:#d2d2d2}

  .sec-title{font-family:"Rokkitt",serif;font-weight:300;font-size:26px;color:var(--red)}
  .services-title{left:121px;top:674px}
  .thumb{width:303px;height:108px;background:#fff;box-shadow:0 0 3px rgba(0,0,0,.25);padding:6px}
  .thumb div{width:100%;height:100%}
  .t1{left:119px;top:715px}
  .t1 div{background:linear-gradient(#c9d0d6 0%,#b8c0c6 30%,#6b6e70 45%,#3a3b3c 100%)}
  .t2{left:448px;top:715px;width:296px}
  .t2 div{background:linear-gradient(120deg,#0c1640,#2a4aa8 40%,#0a1030 70%,#2a56c8)}
  .card-h{font-family:"Arimo",sans-serif;font-weight:700;font-size:18px;color:#333;top:836px}
  .card-p{top:867px;width:300px;font-size:14px;line-height:22.5px;color:#666;text-align:justify}
  .btn{height:31px;border-radius:3px;color:#fff;font-family:"Ubuntu",sans-serif;font-weight:500;font-size:13.5px;line-height:31px;text-align:center;top:967px;width:98px;box-shadow:0 1px 2px rgba(0,0,0,.3)}
  .btn.dark{background:linear-gradient(#3a3a3a,#111)}
  .btn.red{background:linear-gradient(var(--red-light),var(--red-dark))}

  .divider{left:768px;top:665px;width:6px;height:345px;background:radial-gradient(ellipse at left,rgba(0,0,0,.12),transparent 70%)}
  .contact-title{left:804px;top:672px}
  .contact-text{left:806px;top:713px;width:274px;font-family:"Ubuntu",sans-serif;font-size:14px;line-height:17.5px;color:#333;letter-spacing:.45px}
  .field{left:805px;width:273px;background:var(--field);border-radius:3px;box-shadow:inset 0 1px 2px rgba(0,0,0,.35);color:#fff;font-family:"Arimo",sans-serif;font-size:15px;padding:5px 14px}
  .f1{top:783px;height:24px;padding-top:3px}
  .f2{top:816px;height:24px;padding-top:3px}
  .f3{top:850px;height:106px;padding-top:7px}

  .footer{left:0;top:1040px;width:1200px;height:81px;background:var(--footer);box-shadow:inset 0 4px 4px -2px rgba(0,0,0,.15)}
  .footer-links{text-align:center;margin-top:17px;font-family:"Ubuntu",sans-serif;font-weight:500;font-size:16px;color:#555;word-spacing:1px}
  .footer-copy{text-align:center;margin-top:15px;font-family:"Ubuntu",sans-serif;font-size:14px;color:#555;letter-spacing:.3px}
</style>
</head>
<body>
  <header>
    <div class="abs brand"><span>lantern</span><span class="brand-dot"></span></div>
    <div class="abs phone">555-010-2040</div>
    <div class="abs search">Start searching...
      <svg width="14" height="14" viewBox="0 0 14 14"><circle cx="8" cy="6" r="4.5" fill="none" stroke="#ccc" stroke-width="1.5"/><line x1="4.8" y1="9.2" x2="1.5" y2="12.5" stroke="#ccc" stroke-width="1.8"/></svg>
    </div>
  </header>

  <nav class="abs nav">
    <ul>
      <li class="active">HOME</li>
      <li>WHO WE ARE?</li>
      <li>CROSS THE LANTERN</li>
      <li>PERFORMANCE SOLUTIONS</li>
      <li>SUSTAIN SOLUTIONS</li>
      <li>JOIN US</li>
    </ul>
  </nav>

  <section class="intro-video">
    <div class="abs hero" role="img" aria-label="Intro video area: night highway with long-exposure light trails of traffic"></div>
    <div class="abs hero-light"></div>
    <svg class="abs play" width="70" height="70" viewBox="0 0 70 70" aria-label="Play intro video"><circle cx="35" cy="35" r="33" fill="rgba(0,0,0,.45)" stroke="#fff" stroke-width="2"/><polygon points="28,22 50,35 28,48" fill="#fff"/></svg>
    <div class="abs caption">
      <p>"There are managers so preoccupied with their e-mail messages that they never look up from their screens to see what's happening in the nondigital world."</p>
      <p class="by">- Elias Marrow</p>
    </div>
    <div class="abs dots"><span></span><span class="on"></span><span></span><span></span></div>
  </section>

  <main>
    <h1 class="abs welcome"><span>Welcome to <em>Lantern Performance Group</em></span><i></i></h1>
    <p class="abs intro">Lantern Performance Group Inc. is the leading provider of profit generating and people development solutions. With the hands-on experience of best practices, the state-of-the-art technology and in-depth information we help companies increase their efficiencies and profits. Frank, honest, committed, valuable and rewarding are words that customers use to describe the quality services provided by Lantern Performance Group.</p>
    <div class="abs rule"></div>

    <h2 class="abs sec-title services-title">Our Services And Solutions</h2>
    <div class="abs thumb t1"><div role="img" aria-label="Coastal road curving along the sea"></div></div>
    <div class="abs thumb t2"><div role="img" aria-label="Car interior with blue motion-blurred city lights"></div></div>

    <h3 class="abs card-h" style="left:121px">Performance Solutions</h3>
    <p class="abs card-p" style="left:122px">We will work together with you to identify your needs, challenges and opportunities. We will then recommend the next steps and work with you to develop your bespoke.....</p>
    <div class="abs btn dark" style="left:121px">Read More</div>

    <h3 class="abs card-h" style="left:448px">Sustain Solutions</h3>
    <p class="abs card-p" style="left:449px;width:294px">We understand that consulting and training work very well when on site but we also under-stand that some learning can be accomplished as effectively by other means.......</p>
    <div class="abs btn red" style="left:449px">Read More</div>

    <div class="abs divider"></div>
    <h2 class="abs sec-title contact-title">Cross the Lantern</h2>
    <svg class="abs" style="left:1030px;top:678px" width="32" height="22" viewBox="0 0 32 22"><rect x="1" y="1" width="30" height="20" fill="#fff" stroke="#555" stroke-width="1.2"/><polyline points="1,1 16,13 31,1" fill="none" stroke="#555" stroke-width="1.2"/><path d="M1 21 12 10 M31 21 20 10" fill="none" stroke="#555" stroke-width="1"/></svg>
    <p class="abs contact-text">Contact us with your request and we will make sure your needs are met as soon as possible.</p>
    <div class="abs field f1">Name</div>
    <div class="abs field f2">E-mail</div>
    <div class="abs field f3">Comments</div>
    <div class="abs btn dark" style="left:805px">Send it!!</div>
  </main>

  <footer class="abs footer">
    <p class="footer-links">Home &nbsp; | &nbsp; Who We Are? &nbsp; | &nbsp; Cross The Lantern &nbsp; | &nbsp; Performane Solutions &nbsp; | &nbsp; Sustain Solutions &nbsp; | &nbsp; Join Us</p>
    <p class="footer-copy">Copyright © 2012 lantern-outcomes.com. All Rights Reserved.</p>
  </footer>
</body>
</html>
```